Cannabis Dispensary Menu - Digital TV Display

This will be posted in a store on a tv to display all the products they have.
I have all the menu items added to a .psd file for you to work with already. I'm just looking for a good looking design thats also readable. The image size should be 1,920 x 1,080 pixels so that it displays well on a TV. I'd like categories/sub-categories to be separated from each other with some design elements. Another idea to save space would be to replace the CBD: and THC: labels with some kind of small icon that represents them

Target Market(s)

Cannabis consumers

Industry/Entity Type

Cannabis

Font styles to use
Sans Serif

Requirements
Must have
• The menu changes frequently so I will need a finished file I can edit.

```html
<!DOCTYPE html>
<html lang="en">
<head>
<meta charset="utf-8">
<title>Harborleaf Wellness Co – Dispensary Menu</title>
<link rel="stylesheet" href="https://fonts.googleapis.com/css2?family=Anton&family=Bebas+Neue&family=Poppins:wght@400;500;600;700;800&display=swap">
<style>
  :root{
    --page:#e4e4e4;
    --white:#ffffff;
    --paper:#f3f3f0;
    --forest:#1f3d33;
    --forest-text:#1f4a3c;
    --leaf:#2e8a34;
    --lime:#6cbf2a;
    --tomato:#e35a40;
    --tangerine:#f6954b;
    --sativa:#2f7d3a;
    --citron:#d6d420;
    --badge:#1c6b23;
  }
  *{box-sizing:border-box;margin:0;padding:0}
  html,body{width:800px;height:1200px;overflow:hidden;background:var(--page)}
  body{font-family:"Poppins",sans-serif;color:var(--forest-text)}
  .stage{position:absolute;left:0;top:375px;width:800px;height:450px;overflow:hidden}
  .menu{position:absolute;left:0;top:0;width:1600px;height:900px;transform:scale(.5);transform-origin:0 0;background:var(--white);overflow:hidden}
  .abs{position:absolute}
  .paper{left:1000px;top:0;width:600px;height:900px;background:var(--paper)}
  .leaves{left:1160px;top:0;width:440px;height:430px;background:radial-gradient(ellipse at 70% 35%,#4f8f2c 0%,#6ea23f 40%,rgba(120,170,70,.35) 70%,rgba(243,243,240,0) 85%)}
  .brand{left:58px;top:38px;width:270px;font:800 38px/1.02 "Poppins",sans-serif;color:var(--forest-text);text-align:right}
  .brand span{display:block}
  .title{left:345px;top:28px;font:400 126px/1 "Anton",sans-serif;letter-spacing:-1px;color:var(--forest-text);white-space:nowrap}
  .title em{font-style:normal;color:var(--leaf)}
  .vbadge{background:var(--forest);border-radius:14px;color:var(--white);display:flex;align-items:center;justify-content:center}
  .vbadge span{transform:rotate(-90deg);white-space:nowrap;font:400 44px/1 "Bebas Neue",sans-serif;letter-spacing:1px}
  .vbadge b{color:var(--tangerine);font-weight:400}
  .box{border-radius:6px;color:var(--white);padding:10px 14px}
  .box h3{font:700 15px/1 "Poppins",sans-serif;display:flex;align-items:center;gap:6px;margin-bottom:6px;text-transform:uppercase}
  .dot{width:12px;height:12px;border-radius:50%;background:var(--white);display:inline-block;flex:none}
  .indica{background:var(--tomato)} .hybrid{background:var(--tangerine)} .sativa{background:var(--sativa)} .cbd{background:var(--citron)}
  .cols{display:flex;gap:26px}
  .line{display:flex;justify-content:space-between;align-items:center;font:400 13px/16.5px "Poppins",sans-serif;white-space:nowrap}
  .pct{background:var(--badge);color:var(--white);font:600 9px/1 "Poppins",sans-serif;padding:2px 3px;min-width:26px;text-align:center;margin-left:8px}
  .rule{height:2px;background:var(--forest)}
  .deal{left:145px;top:748px;font:700 30px/1 "Poppins",sans-serif;color:var(--forest-text)}
  .deal small{font-weight:400;font-size:26px}
  .dealnames{left:145px;top:796px;display:flex;gap:40px;font:400 13px/15px "Poppins",sans-serif}
  .photo{border-radius:50%}
  .panel-text{color:var(--white)}
  .conc-title{left:577px;top:214px;font:400 46px/1 "Bebas Neue",sans-serif;color:var(--lime)}
  .sub{font:700 18px/1 "Poppins",sans-serif;color:var(--white);display:flex;align-items:center;gap:8px;text-transform:uppercase}
  .sub i{width:8px;height:8px;background:var(--lime);border-radius:50%;display:inline-block}
  .price{font:700 20px/1 "Poppins",sans-serif;color:var(--white)}
  .price b{color:var(--lime);font-weight:700}
  .tile{width:82px;height:88px;border-radius:6px;text-align:center;color:var(--white);padding-top:8px}
  .tile h4{font:600 13px/1 "Poppins",sans-serif;margin-bottom:5px}
  .tile .dot{width:14px;height:14px}
  .tile p{font:400 9.5px/1.1 "Poppins",sans-serif;margin-top:4px}
  .tile.s{background:var(--sativa)}
  .divider{height:1px;background:rgba(255,255,255,.55);width:440px;left:577px}
  .small{font:400 13px/17px "Poppins",sans-serif;color:var(--white)}
  .small b{font-weight:700}
  .small em{font-style:normal;color:var(--lime);font-weight:600}
  .pline{display:flex;align-items:center;font:400 12px/19px "Poppins",sans-serif;color:var(--white);white-space:nowrap}
  .pline .pct{background:var(--leaf)}
  .sec{font:400 46px/1 "Bebas Neue",sans-serif;color:var(--forest-text);letter-spacing:.5px}
  .list .line{font-size:11.5px;line-height:15.6px}
</style>
</head>
<body>
<div class="stage">
<main class="menu">

  <div class="abs paper"></div>
  <div class="abs leaves" role="img" aria-label="Photo of green cannabis leaves in the top right corner"></div>

  <div class="abs brand"><span>Harborleaf</span><span>Wellness Co</span></div>
  <h1 class="abs title">DISPENSARY <em>MENU</em></h1>

  <!-- Flower section -->
  <div class="abs vbadge" style="left:58px;top:186px;width:60px;height:372px"><span>FLOWER <b>$50</b> OZ'S</span></div>

  <section class="abs box indica" style="left:134px;top:186px;width:360px;height:180px">
    <h3><span class="dot"></span>Indica</h3>
    <div class="cols">
      <div style="width:150px">
        <div class="line">Blueberry<span class="pct">28%</span></div>
        <div class="line">Purple Vapor<span class="pct">27%</span></div>
        <div class="line">Purple Kush<span class="pct">26%</span></div>
        <div class="line">Ice Cream Cake<span class="pct">25%</span></div>
        <div class="line">Garlic Breath<span class="pct">24%</span></div>
        <div class="line">Master Kush<span class="pct">24%</span></div>
        <div class="line">Kushy Kush<span class="pct">24%</span></div>
        <div class="line">G13 Haze<span class="pct">24%</span></div>
      </div>
      <div style="width:152px;padding-top:16px">
        <div class="line">Island Pink Kush<span class="pct">24%</span></div>
        <div class="line">Green Crack<span class="pct">24%</span></div>
        <div class="line">White Rhino<span class="pct">24%</span></div>
        <div class="line">Pink Kush<span class="pct">21%</span></div>
        <div class="line">Grape Ape<span class="pct">21%</span></div>
        <div class="line">Peyote Cookies<span class="pct">22%</span></div>
        <div class="line">God Bud<span class="pct">20%</span></div>
      </div>
    </div>
  </section>

  <section class="abs box hybrid" style="left:134px;top:376px;width:360px;height:95px">
    <h3><span class="dot"></span>Hybrid</h3>
    <div class="cols">
      <div style="width:150px">
        <div class="line" style="font-size:11.5px;line-height:15px">Trail Scout Cookies<span class="pct">28%</span></div>
        <div class="line" style="font-size:11.5px;line-height:15px">Peanutbutter Breath<span class="pct">28%</span></div>
        <div class="line" style="font-size:11.5px;line-height:15px">Tangie<span class="pct">28%</span></div>
        <div class="line" style="font-size:11.5px;line-height:15px">White Widow<span class="pct">26%</span></div>
      </div>
      <div style="width:152px">
        <div class="line" style="font-size:11.5px;line-height:15px">Gelato<span class="pct">25%</span></div>
        <div class="line" style="font-size:11.5px;line-height:15px">Miracle Alien Cookies<span class="pct">22%</span></div>
        <div class="line" style="font-size:11.5px;line-height:15px">Chem Dog<span class="pct">19%</span></div>
        <div class="line" style="font-size:11.5px;line-height:15px">Grape God<span class="pct">20%</span></div>
      </div>
    </div>
  </section>

  <section class="abs box sativa" style="left:134px;top:481px;width:154px;height:77px">
    <h3><span class="dot"></span>Sativa</h3>
    <div class="line" style="line-height:15px">King Tut</div>
    <div class="line" style="line-height:15px">Big Banner</div>
    <div class="line" style="line-height:15px">Pineapple Express</div>
  </section>

  <section class="abs box cbd" style="left:319px;top:481px;width:175px;height:77px;color:var(--forest-text)">
    <h3><span class="dot" style="background:var(--forest-text)"></span>CBD</h3>
    <div class="line" style="line-height:14px">Candida</div>
    <div class="line" style="line-height:14px">CBD<span class="pct">20%</span></div>
    <div class="line" style="line-height:14px">THC<span class="pct">0.01%</span></div>
  </section>

  <div class="abs rule" style="left:58px;top:570px;width:436px"></div>

  <section class="abs box indica" style="left:60px;top:579px;width:178px;height:115px;padding:8px 10px">
    <h3 style="margin-bottom:3px"><span class="dot"></span>Indica</h3>
    <div class="line" style="line-height:15px">Tall Fern Pink Kush<span class="pct">28%</span></div>
    <div class="line" style="line-height:15px">3.5g<span class="pct">25%</span></div>
    <div class="line" style="line-height:15px">7g<span class="pct">45%</span></div>
    <div class="line" style="line-height:15px">14g<span class="pct">85%</span></div>
    <div class="line" style="line-height:15px">28g<span class="pct">108%</span></div>
  </section>

  <section class="abs box hybrid" style="left:257px;top:579px;width:177px;height:115px;padding:8px 10px">
    <h3 style="margin-bottom:3px"><span class="dot"></span>Hybrid</h3>
    <div class="line" style="line-height:15px">Kalani Kush<span class="pct">30%</span></div>
    <div class="line" style="line-height:15px">3.5g<span class="pct">30%</span></div>
    <div class="line" style="line-height:15px">7g<span class="pct">50%</span></div>
    <div class="line" style="line-height:15px">14g<span class="pct">90%</span></div>
    <div class="line" style="line-height:15px">28g<span class="pct">160%</span></div>
  </section>

  <div class="abs vbadge" style="left:450px;top:579px;width:44px;height:115px;border-radius:8px"><span style="font-size:34px">AAAA+</span></div>

  <div class="abs rule" style="left:58px;top:708px;width:436px"></div>

  <div class="abs vbadge" style="left:58px;top:719px;width:60px;height:121px"><span style="font-size:34px">PER ROLLS</span></div>
  <div class="abs deal">1–$5 <small>or</small> 2–$8</div>
  <div class="abs dealnames">
    <div>JKP<br>Kushy Kush<br>Master Kush</div>
    <div>Grape Ape<br>Green Crack<br>White Widow</div>
  </div>
  <div class="abs photo" style="left:384px;top:728px;width:122px;height:105px;background:radial-gradient(circle at 45% 45%,#7c8a3c,#4f5e28 60%,rgba(255,255,255,0) 72%)" role="img" aria-label="Photo of a dried cannabis bud"></div>

  <!-- Concentrates panel -->
  <svg class="abs" style="left:0;top:0" width="1600" height="900" viewBox="0 0 1600 900" aria-hidden="true">
    <polygon fill="#1f3d33" points="555,186 1020,186 1048,216 1020,246 1048,276 1020,306 1048,336 1020,366 1048,396 1020,426 1048,456 1020,486 1048,516 1020,546 1048,576 1020,606 1048,636 1020,666 1048,696 1020,726 1048,756 1020,786 1048,816 1020,846 1048,876 1020,900 555,900 527,876 555,846 527,816 555,786 527,756 555,726 527,696 555,666 527,636 555,606 527,576 555,546 527,516 555,486 527,456 555,426 527,396 555,366 527,336 555,306 527,276 555,246 527,216"/>
  </svg>

  <h2 class="abs conc-title">CONCENTRATES</h2>

  <div class="abs sub" style="left:577px;top:270px"><i></i>Live Resin</div>
  <div class="abs price" style="left:818px;top:268px">1g – <b>$30</b> or 5g – <b>$100</b></div>
  <div class="abs tile indica" style="left:577px;top:301px"><h4>(INDICA)</h4><span class="dot"></span><p>Blackberry</p></div>
  <div class="abs tile hybrid" style="left:667px;top:301px"><h4>(HYBRID)</h4><span class="dot"></span><p>Blue Dream<br>Gummy Bear<br>Big Banner</p></div>
  <div class="abs tile s" style="left:757px;top:301px"><h4>(SATIVA)</h4><span class="dot"></span><p>Solar<br>Star</p></div>
  <div class="abs photo" style="left:910px;top:310px;width:80px;height:80px;background:radial-gradient(circle,#eef2ea 55%,#cfd6c8 75%,rgba(31,61,51,0) 77%)" role="img" aria-label="Photo of a dish with a cannabis leaf"></div>
  <div class="abs divider" style="top:400px"></div>

  <div class="abs sub" style="left:577px;top:409px"><i></i>Shatter</div>
  <div class="abs price" style="left:818px;top:407px">1g – <b>$30</b> or 5g – <b>$100</b></div>
  <div class="abs tile indica" style="left:577px;top:437px"><h4>(INDICA)</h4><span class="dot"></span><p>Bubba Kush<br>Death Star</p></div>
  <div class="abs tile hybrid" style="left:667px;top:437px"><h4>(HYBRID)</h4><span class="dot"></span><p>M.A.C. 1<br>Biscotti</p></div>
  <div class="abs tile s" style="left:757px;top:437px"><h4>(SATIVA)</h4><span class="dot"></span><p>Amnesia<br>Haze</p></div>
  <div class="abs photo" style="left:912px;top:447px;width:78px;height:78px;background:radial-gradient(circle at 45% 40%,#d9b21c,#a98510 65%,rgba(31,61,51,0) 72%)" role="img" aria-label="Photo of amber cannabis oil in a dish"></div>
  <div class="abs divider" style="top:537px"></div>

  <div class="abs sub" style="left:577px;top:556px"><i></i>Diamonds</div>
  <div class="abs small" style="left:577px;top:580px">THCA Diamonds<br>3.5g – <em>$50</em></div>
  <div class="abs sub" style="left:750px;top:556px"><i></i>Oil</div>
  <div class="abs small" style="left:750px;top:580px">1g – <em>$30</em> | 3g – <em>$100</em> |<br>5g <em>$200</em></div>
  <div class="abs" style="left:945px;top:542px;width:36px;height:84px;border-radius:6px;background:linear-gradient(#2a2a2a 0 28%,#f4f4f4 28%)" role="img" aria-label="Photo of a dropper bottle with a leaf"></div>
  <div class="abs divider" style="top:629px"></div>

  <div class="abs sub" style="left:577px;top:644px"><i></i>Hash</div>
  <div class="abs" style="left:577px;top:666px">
    <div class="small"><b>Black Magic</b></div>
    <div class="pline" style="width:130px;justify-content:space-between">1g<span class="pct">15%</span></div>
    <div class="pline" style="width:130px;justify-content:space-between">5g<span class="pct">50%</span></div>
  </div>
  <div class="abs" style="left:751px;top:666px">
    <div class="small"><b>XXX</b></div>
    <div class="pline" style="width:130px;justify-content:space-between">1g<span class="pct">15%</span></div>
    <div class="pline" style="width:130px;justify-content:space-between">5g<span class="pct">50%</span></div>
  </div>
  <div class="abs" style="left:912px;top:666px">
    <div class="small"><b>XX</b></div>
    <div class="pline" style="width:100px;justify-content:space-between">1g<span class="pct">7%</span></div>
    <div class="pline" style="width:100px;justify-content:space-between">5g<span class="pct">25%</span></div>
  </div>
  <div class="abs divider" style="top:735px"></div>

  <div class="abs sub" style="left:577px;top:748px"><i></i>Vapes</div>
  <div class="abs" style="left:577px;top:776px">
    <div class="small"><b>Skyline 1g</b></div>
    <div class="pline" style="width:130px;justify-content:space-between">Distillate<span class="pct">35%</span></div>
    <div class="pline" style="width:130px;justify-content:space-between;margin-top:6px">Premium<span class="pct">39%</span></div>
  </div>
  <div class="abs" style="left:751px;top:776px">
    <div class="small"><b>Lights Out 1g</b></div>
    <div class="pline" style="width:130px;justify-content:space-between">1<span class="pct">30%</span></div>
    <div class="pline" style="width:130px;justify-content:space-between;margin-top:6px">3<span class="pct">75%</span></div>
  </div>
  <div class="abs" style="left:912px;top:776px">
    <div class="small"><b>Thunderclap 1g</b></div>
    <div class="pline" style="width:100px;justify-content:space-between">1<span class="pct">30%</span></div>
    <div class="pline" style="width:100px;justify-content:space-between;margin-top:6px">3<span class="pct">75%</span></div>
  </div>

  <!-- Right column -->
  <h2 class="abs sec" style="left:1085px;top:198px">EDIBLES</h2>
  <div class="abs list" style="left:1089px;top:240px;width:190px">
    <div class="line">Shatter Chews 150mg<span class="pct">20%</span></div>
    <div class="line">Shatter Bar 500mg<span class="pct">30%</span></div>
    <div class="line">Fuel Crew Gummies 500mg<span class="pct">25%</span></div>
    <div class="line">Ridgeline Gummies</div>
    <div class="line">500mg<span class="pct">30%</span></div>
    <div class="line">3000mg<span class="pct">50%</span></div>
    <div class="line">West Shore Gummies 600mg<span class="pct">30%</span></div>
    <div class="line">Hemp Pop 60mg 1 - $15 or 3<span class="pct">40%</span></div>
    <div class="line">Hemp Caps</div>
    <div class="line">CBD: 13mg, THC: 145mg<span class="pct">20%</span></div>
    <div class="line">Canna Sugar</div>
    <div class="line">CBD: 15mg, THC: 50mg<span class="pct">5%</span></div>
  </div>
  <div class="abs list" style="left:1336px;top:246px;width:120px;font-weight:400">
    <div class="line">Canna Cookies</div>
    <div class="line">50mg - <b>$5</b></div>
    <div class="line">100mg - <b>$10</b></div>
    <div class="line">156mg - <b>$15</b></div>
    <div class="line">HWC Chocolates</div>
    <div class="line">100mg - <b>$10</b></div>
    <div class="line">150mg - <b>$15</b></div>
    <div class="line">250mg - <b>$25</b></div>
    <div class="line">HWC Gummies</div>
    <div class="line">20mg - <b>$2</b></div>
    <div class="line">100mg - <b>$10</b></div>
    <div class="line">200mg - <b>$20</b></div>
    <div class="line">300mg - <b>$30</b></div>
  </div>

  <h2 class="abs sec" style="left:1085px;top:458px">HOLISTIC HEALTH ESSENTIALS</h2>
  <div class="abs list" style="left:1089px;top:498px;width:170px">
    <div class="line">Topical Cream</div>
    <div class="line">THC: 500mg CBD: 50mg</div>
    <div class="line">Small<span class="pct">10%</span></div>
    <div class="line">Large<span class="pct">25%</span></div>
    <div class="line">Bath Bombs CBD: 10mg</div>
    <div class="line">THC: 50mg<span class="pct">5%</span></div>
    <div class="line">THC: 100mg<span class="pct">10%</span></div>
    <div class="line">THC: 150mg<span class="pct">15%</span></div>
  </div>
  <div class="abs list" style="left:1337px;top:498px;width:178px">
    <div class="line">CBD Oil</div>
    <div class="line">CBD: 1000mg<span class="pct">40%</span></div>
    <div class="line">CBD: 5000mg<span class="pct">200%</span></div>
    <div class="line">CBD VG Tincture</div>
    <div class="line">CBD: 200mg THC: 60mg<span class="pct">40%</span></div>
    <div class="line">THC VG Tincture</div>
    <div class="line">CBD: 13mg THC: 450mg<span class="pct">40%</span></div>
    <div class="line">CBD Patch CBD: 20mg<span class="pct">20%</span></div>
    <div class="line">CBD Cream CBD: 3000mg<span class="pct">20%</span></div>
  </div>

  <h2 class="abs sec" style="left:1085px;top:640px">PET CARE</h2>
  <div class="abs" style="left:1089px;top:684px;font:400 14px/16px 'Poppins',sans-serif">
    <b style="font-weight:700">CBD Cat Treats</b><br>THC: 0.5mg<br>CBD: 5mg<br><b style="font-weight:700">$10</b>
  </div>
  <div class="abs" style="left:1261px;top:684px;font:400 14px/16px 'Poppins',sans-serif">
    <b style="font-weight:700">CBD Dog Treats</b><br>THC:2mg<br>CBD: 5.6mg<br><b style="font-weight:700">$10</b>
  </div>

  <h2 class="abs sec" style="left:1085px;top:770px">SEASONAL</h2>
  <div class="abs list" style="left:1089px;top:816px;width:280px">
    <div class="line" style="font-size:13px">Christmas THC Crackers<span class="pct">15%</span></div>
    <div class="line" style="font-size:13px">Christmas Edible Advent Calendars<span class="pct">80%</span></div>
  </div>

  <div class="abs photo" style="left:1383px;top:640px;width:240px;height:240px;background:radial-gradient(circle at 45% 45%,#f1a21e,#d9780e 55%,#c9b48e 68%,rgba(243,243,240,0) 72%)" role="img" aria-label="Photo of a glass bowl filled with amber softgel capsules"></div>

</main>
</div>
</body>
</html>
```